I am a company selling interior designing materials

HI, I am selling interior design materials and require a namecard which is more outstanding while following a certain details placement as attached.

My clients are mainly interior designers so it has to attract their attention rather than feeling that its "just another namecard". I am selling wallcoverings, fabrics, acoustics and carpets.

Target Market(s)

interior designers designing hotels, commerical offices.

Contact Information for Business Card

As per attached.
Please change address to 47 Jalan 16 Tampines #05-02 Velmora Building Singapore 527314

Font styles to use
Other font styles liked:
• calibri

Requirements
Must have
• (1) company logo on top in the middle. Placement of contac details to be the same
• (2) company color is blue/green cymk 75/8/42/0
• (3) "KTV" logo to be prominent
• (4) You may change the logo but there should be a "swirl" surrounding the word KTV like current logo. The swirl pattern does not need to follow current logo and you may propose.
Should not have
• (1) there should not be any designs above "KTV" logo
• (2) no sharp triangles or angles

```html
<!DOCTYPE html>
<html lang="en">
<head>
<meta charset="utf-8">
<title>KTV Business Card</title>
<link rel="stylesheet" href="https://fonts.googleapis.com/css2?family=Roboto+Slab:wght@700&family=Roboto:wght@400&display=swap">
<style>
  :root {
    --teal: #00918a;
    --teal-deep: #008880;
    --ink: #4a4a4c;
    --text: #2f2f2f;
    --red: #d0302b;
    --card-white: #f6f6f6;
    --backdrop: #c9c9c9;
  }
  * { margin: 0; padding: 0; box-sizing: border-box; }
  html, body {
    width: 1200px;
    height: 576px;
    overflow: hidden;
    background: var(--backdrop);
  }
  .stage {
    position: relative;
    width: 1200px;
    height: 576px;
  }
  .card {
    position: absolute;
    top: 138px;
    width: 484px;
    height: 292px;
    border-radius: 14px;
    overflow: hidden;
    box-shadow: 0 3px 6px rgba(0,0,0,0.25);
  }
  /* Front side */
  .card-front {
    left: 82px;
    background: linear-gradient(180deg, var(--teal) 0%, var(--teal-deep) 100%);
    display: flex;
    align-items: center;
    justify-content: center;
  }
  .front-wordmark {
    font-family: "Roboto Slab", serif;
    font-weight: 700;
    font-size: 62px;
    letter-spacing: 1px;
    color: #ffffff;
  }
  /* Back side */
  .card-back {
    left: 602px;
    background: var(--card-white);
  }
  .brand-block {
    position: absolute;
    left: 20px;
    top: 96px;
    width: 228px;
    text-align: center;
    font-family: "Roboto Slab", serif;
    font-weight: 700;
    color: var(--ink);
  }
  .brand-wordmark {
    font-size: 34px;
    line-height: 1;
    letter-spacing: 1px;
  }
  .brand-name {
    margin-top: 20px;
    font-size: 17px;
    line-height: 1.1;
  }
  .brand-tagline {
    margin-top: 4px;
    display: flex;
    align-items: center;
    justify-content: center;
    gap: 6px;
    font-size: 10px;
  }
  .brand-tagline .rule {
    width: 44px;
    height: 1.5px;
    background: var(--teal);
  }
  .contact {
    position: absolute;
    left: 267px;
    top: 70px;
    font-family: "Roboto", sans-serif;
    color: var(--text);
  }
  .contact-name {
    font-family: "Roboto Slab", serif;
    font-weight: 700;
    font-size: 19px;
    color: var(--teal);
    line-height: 1.2;
  }
  .contact-mobile {
    font-size: 11.5px;
    margin-top: 2px;
  }
  .contact-list {
    list-style: none;
    margin-top: 26px;
  }
  .contact-list li {
    display: flex;
    align-items: center;
    gap: 10px;
    font-size: 11.5px;
    height: 17px;
  }
  .contact-list svg {
    width: 10px;
    height: 10px;
    fill: var(--teal);
    flex: none;
  }
  .contact-address {
    margin-top: 6px;
    font-size: 11.5px;
    line-height: 19px;
  }
  .accent-band {
    position: absolute;
    left: 0;
    right: 0;
    bottom: 0;
    height: 5px;
    display: flex;
  }
  .accent-band .band-teal { width: 300px; background: var(--teal); }
  .accent-band .band-red { flex: 1; background: var(--red); }
</style>
</head>
<body>
<main class="stage">
  <section class="card card-front" aria-label="Card front">
    <span class="front-wordmark">KTV</span>
  </section>

  <section class="card card-back" aria-label="Card back">
    <div class="brand-block">
      <div class="brand-wordmark">KTV</div>
      <div class="brand-name">Kestovia Interior</div>
      <div class="brand-tagline"><span class="rule"></span>Furnishings Pte Ltd<span class="rule"></span></div>
    </div>

    <div class="contact">
      <div class="contact-name">Lena Ho</div>
      <div class="contact-mobile">(65) 9172 4403</div>
      <ul class="contact-list">
        <li>
          <svg viewBox="0 0 10 10" aria-hidden="true"><path d="M1 3.2C1 2 2 1.5 5 1.5S9 2 9 3.2V4H7.2V3.2H2.8V4H1Z M2.5 4.6h5l1.3 3.6H1.2Z"/></svg>
          (65) 6281 5072
        </li>
        <li>
          <svg viewBox="0 0 10 10" aria-hidden="true"><path d="M0.5 2h9v6h-9Z M1.3 2.6 5 5.4 8.7 2.6" fill="none" stroke="#00918a" stroke-width="1"/><path d="M0.5 2h9L5 5.4Z"/></svg>
          lena@ktvfurnishings.com
        </li>
        <li>
          <svg viewBox="0 0 10 10" aria-hidden="true"><circle cx="5" cy="5" r="4.3" fill="none" stroke="#00918a" stroke-width="1"/><ellipse cx="5" cy="5" rx="1.8" ry="4.3" fill="none" stroke="#00918a" stroke-width="0.8"/><path d="M0.7 5h8.6" stroke="#00918a" stroke-width="0.8"/></svg>
          www.ktvfurnishings.com
        </li>
      </ul>
      <p class="contact-address">47 Jalan 16 Tampines #05-02<br>Velmora Building Singapore 527314</p>
    </div>

    <div class="accent-band"><span class="band-teal"></span><span class="band-red"></span></div>
  </section>
</main>
</body>
</html>
```